Label for Dog Nourishing CBD Balm

Dear Designers,

We are looking for a packaging expert to design our new Hydrating Balm for dogs which contain a relaxing hemp extract (CBD). The product is intended to be massaged on the dog’s paws to make them softer and promote the animal’s well-being :)

Our company is already selling various relaxing cat & dog products, and we would like this new design to reflect the same "style & feeling" as our current products (see attached ZIP file).

Technical aspects:
- The packaging is a 40ml aluminium jar (58mm x 23mm).
- We are looking to design 2 separate labels (one for the front, one for the back)
- The label dimensions should be : 50mm x 50mm
- Please follow technical guidelines from printer (see ZIP file).

Design aspects:
- The design should be compatible with our brand identity (i.e. fluffly, pure, relaxing, positive, clean & natural).
- People should understand what the product "is" and what the product "does" simply from looking at the design.
- The actual balm is white/yellow in color.
- Soft/rounded shapes are preferred.
- Please use our brand's colors (see typo & colors in ZIP file)
- Please use our brand's fonts (see typo & colors in ZIP file)
- Please use our company logo (see ZIP file).
- The design also needs to convey a strong sense of professionalism as we are an animal "healthcare" brand.
- If you want to include a dog picture, we would prefer you to use a picture of our official brand ambassador (see ZIP file).
- Only original work (no plagiarism will be accepted).

Please don't hesitate to send us a message if you have any questions about the brand, the product or the design requirements.

We look forward to seeing your designs & working on this together !

Thanks & regards,
Marcus

Target Market(s)

Dog owners

Font styles to use
Other font styles liked:
• See ZIP file

Requirements
Must have
• Brand fonts (see typo & colors in ZIP file)
Brand colors (see typo & colors in ZIP file)

```html
<!DOCTYPE html>
<html lang="en">
<head>
<meta charset="utf-8">
<title>Verdalia VerdaBalm Soothing Balm – Front and Back Labels</title>
<link rel="stylesheet" href="https://fonts.googleapis.com/css2?family=Montserrat:ital,wght@0,400;0,500;0,600;0,700;0,800;1,400&display=swap">
<style>
  :root {
    --backdrop: #3b3b3d;
    --brand-green: #3aa384;
    --deep-green: #17301e;
    --ink: #1c2620;
    --paper: #ffffff;
    --coat: #ece9e6;
    --coat-shade: #d3cdc8;
  }
  * { box-sizing: border-box; margin: 0; padding: 0; }
  html, body { width: 1200px; height: 619px; overflow: hidden; }
  body {
    background: var(--backdrop);
    font-family: "Montserrat", sans-serif;
    color: var(--ink);
    position: relative;
  }
  .label {
    position: absolute;
    top: 95px;
    width: 430px;
    height: 430px;
    border-radius: 50%;
    background: var(--brand-green);
    overflow: hidden;
  }
  .label--front { left: 125px; }
  .label--back { left: 645px; }
  .label__face {
    position: absolute;
    inset: 13px;
    border-radius: 50%;
    background: var(--paper);
    overflow: hidden;
  }

  /* Brand name stand-in */
  .brand {
    position: absolute;
    display: flex;
    align-items: center;
    gap: 6px;
    font-weight: 600;
    color: var(--deep-green);
    letter-spacing: 0.5px;
    white-space: nowrap;
  }
  .brand__dot {
    width: 10px; height: 10px;
    border-radius: 50%;
    background: var(--brand-green);
  }

  /* Front label */
  .front__swoosh { position: absolute; left: 0; top: 0; }
  .front__ambassador {
    position: absolute;
    left: 4px; top: 64px;
    width: 198px; height: 206px;
    background: linear-gradient(160deg, var(--coat) 0%, var(--coat-shade) 100%);
    border-radius: 40% 55% 0 0;
  }
  .front .brand {
    right: 84px; top: 112px;
    font-size: 21px;
  }
  .front__line {
    position: absolute;
    right: 30px; top: 148px;
    font-style: italic;
    font-weight: 400;
    font-size: 26px;
    color: var(--ink);
  }
  .front__title {
    position: absolute;
    right: 30px; top: 180px;
    text-align: right;
    font-weight: 800;
    font-size: 46px;
    line-height: 42px;
    color: var(--deep-green);
    letter-spacing: -0.5px;
  }
  .front__claims {
    position: absolute;
    left: 24px; right: 24px; top: 269px;
    height: 41px;
    background: var(--deep-green);
    clip-path: polygon(3% 0, 97% 0, 100% 100%, 0 100%);
    color: var(--paper);
    font-weight: 700;
    font-size: 19px;
    display: flex; align-items: center; justify-content: center;
    letter-spacing: 0.3px;
  }
  .front__dose {
    position: absolute;
    left: 0; right: 0; top: 310px;
    height: 45px;
    background: var(--brand-green);
    color: var(--deep-green);
    font-weight: 700;
    font-size: 21px;
    display: flex; align-items: center; justify-content: center;
  }
  .front__weight {
    position: absolute;
    left: 0; right: 0; top: 355px;
    height: 50px;
    background: var(--deep-green);
    clip-path: polygon(17% 0, 83% 0, 70% 100%, 30% 100%);
    color: var(--brand-green);
    font-weight: 500;
    font-size: 26px;
    display: flex; align-items: center; justify-content: center;
  }

  /* Back label */
  .back .brand {
    left: 50%; top: 50px;
    transform: translateX(-50%);
    font-size: 21px;
  }
  .back__copy {
    position: absolute;
    left: 16px; right: 16px; top: 92px;
    text-align: center;
  }
  .back__heading {
    color: var(--brand-green);
    font-weight: 500;
    font-size: 17px;
    line-height: 20px;
    letter-spacing: 0.2px;
  }
  .back__text {
    font-size: 11.2px;
    font-weight: 500;
    line-height: 14.5px;
  }
  .back__section + .back__section { margin-top: 12px; }
</style>
</head>
<body>

  <section class="label label--front front" aria-label="Front label">
    <div class="label__face">
      <svg class="front__swoosh" width="404" height="404" viewBox="0 0 404 404" aria-hidden="true">
        <path d="M91 38 H292 C310 38 318 44 319 72 C321 48 328 41 344 37"
              fill="none" stroke="var(--brand-green)" stroke-width="7" stroke-linecap="round"/>
      </svg>
      <div class="front__ambassador" role="img" aria-label="Photo of the white wrinkled brand ambassador dog seen in profile"></div>
      <div class="brand"><span class="brand__dot"></span>VERDALIA</div>
      <p class="front__line">VerdaBalm</p>
      <h1 class="front__title">SOOTHING<br>BALM</h1>
      <p class="front__claims">REPAIR | NOURISH | PROTECT</p>
      <p class="front__dose">CBD 250MG | 0% THC</p>
      <p class="front__weight">40g</p>
    </div>
  </section>

  <section class="label label--back back" aria-label="Back label">
    <div class="label__face">
      <div class="brand"><span class="brand__dot"></span>VERDALIA</div>
      <div class="back__copy">
        <div class="back__section">
          <h2 class="back__heading">EVERYDAY RELAXATION</h2>
          <p class="back__text">This balm repairs, nourishes and protects your<br>dog's sensitive skin. Its trusted multi-action formula<br>brings relief to fragile areas and soothes temporary irrations<br>(paw pads, elbows, etc.)</p>
        </div>
        <div class="back__section">
          <h2 class="back__heading">RECOMMENDED USE:</h2>
          <p class="back__text">Rub a small amount of balm in the palm of your hand and<br>apply to sensitive areas as a daily care ritual. Repeat until the<br>product has been completely absorbed.</p>
        </div>
        <div class="back__section">
          <h2 class="back__heading">INGREDIENTS:</h2>
          <p class="back__text">Shea Butter, Beeswax, Coconut Oil, Hemp Extract (0% THC).</p>
        </div>
        <div class="back__section">
          <h2 class="back__heading">Distributed by:</h2>
          <p class="back__text">VERDA EUROPE KFT.<br>Lomb utca 14, 1071 Budapest<br>Hungary</p>
        </div>
      </div>
    </div>
  </section>

</body>
</html>
```